M&A Advisory firm needs elegant and powerful letterhead

We need a powerful but elegant letterhead to engage with the international financial industry.

Target Market(s)

New York and International Financial Industry

Industry/Entity Type

Finance

Font styles to use
Other font styles liked:
• Poppins

Requirements
Must have
• 482 W 71st Street 14th Floor New York, NY 10157 O: +1 (212) 555 0147 F: +1 (212) 555 0182

```html
<!DOCTYPE html>
<html lang="en">
<head>
<meta charset="UTF-8">
<title>Halvern Letterhead</title>
<link rel="stylesheet" href="https://fonts.googleapis.com/css2?family=Poppins:wght@400&display=swap">
<style>
  :root {
    --brand-blue: #0a5494;
    --rule-grey: #c8c8c8;
    --paper: #ffffff;
  }
  html, body {
    margin: 0;
    padding: 0;
    overflow: hidden;
    background: var(--paper);
  }
  .letterhead {
    position: relative;
    width: 848px;
    height: 1200px;
    background: var(--paper);
    font-family: 'Poppins', sans-serif;
    color: var(--brand-blue);
    overflow: hidden;
  }
  .brand {
    position: absolute;
    left: 116px;
    top: 52px;
    display: flex;
    align-items: center;
    gap: 14px;
  }
  .brand-dot {
    width: 40px;
    height: 40px;
    border-radius: 50%;
    background: var(--brand-blue);
  }
  .brand-name {
    font-size: 41px;
    font-weight: 400;
    line-height: 1;
    letter-spacing: 0.5px;
    color: var(--brand-blue);
  }
  .rule {
    position: absolute;
    height: 3px;
    background: var(--rule-grey);
  }
  .rule .accent {
    position: absolute;
    left: 0;
    top: 0;
    height: 100%;
    width: 59px;
    background: var(--brand-blue);
  }
  .rule-header { left: 113px; top: 108px; width: 629px; }
  .rule-footer { left: 110px; top: 1068px; width: 628px; }
  .contact {
    position: absolute;
    left: 110px;
    top: 1085px;
    margin: 0;
    font-size: 14.5px;
    font-weight: 400;
    line-height: 24.7px;
    font-style: normal;
  }
  .contact span { display: block; }
  .footer-band {
    position: absolute;
    left: 0;
    bottom: 0;
    width: 848px;
    height: 36px;
    background: var(--brand-blue);
  }
</style>
</head>
<body>
  <div class="letterhead">
    <header class="brand">
      <div class="brand-dot"></div>
      <div class="brand-name">HALVERN</div>
    </header>
    <div class="rule rule-header"><div class="accent"></div></div>

    <div class="rule rule-footer"><div class="accent"></div></div>
    <address class="contact">
      <span class="contact-address">482 W 71st Street 14th Floor New York, NY 10157</span>
      <span class="contact-office">O: +1 (212) 555 0147</span>
      <span class="contact-fax">F: +1 (212) 555 0182</span>
    </address>
    <div class="footer-band"></div>
  </div>
</body>
</html>
```